Corporate Design für Austausch & Neuerrichtung von Heizungs- und Klimatechnik
Zielgruppe
Austausch, Neuerrichtung modernster Heizungstechnik und Klimatechnik
Unsere Zielgruppe sind Privatpersonen die Ihr Haus zukunftsorientiert beheizen bzw. kühlen wollen
Aufgabenstellung
schlicht, modern, klar
gerne schwarzer Hintergrund und max 3 Farben gerne auch kräftig / auffällig
Nur eine Idee: Vielleicht können kleine Icons im Logo erscheinen.... z.b. 4 Elemente.... Feuer, Wasser, Luft, Erde plus schneeflocke für die klimatechnik (?)

```html
<!DOCTYPE html>
<html lang="de">
<head>
<meta charset="utf-8">
<title>Thermfeld – Corporate Design</title>
<link href="https://fonts.googleapis.com/css2?family=Ubuntu:wght@400;500&display=swap" rel="stylesheet">
<style>
  :root{
    --red:#e30613;
    --grey:#a6a6a6;
    --ink:#1d1d1b;
    --paper:#fff;
    --rule:#b9b9b9;
  }
  *{margin:0;padding:0;box-sizing:border-box}
  html,body{width:896px;height:1200px;overflow:hidden;background:var(--paper)}
  body{position:relative;font-family:"Ubuntu",sans-serif;color:var(--ink)}

  .dark{background:radial-gradient(ellipse at 50% 50%,#2b2a28 0%,#141311 45%,#000 80%)}

  /* brand lockup */
  .brand{display:flex;align-items:center;position:absolute}
  .brand-dot{border-radius:50%;border:solid var(--red);flex:none}
  .brand-name{color:var(--red);font-weight:500;line-height:1;white-space:nowrap}
  .brand-tagline{color:var(--grey);font-weight:400;line-height:1.1;white-space:nowrap}

  /* hero banner */
  .hero{position:absolute;left:18px;top:17px;width:856px;height:454px}
  .hero .brand{left:180px;top:178px}
  .hero .brand-dot{width:108px;height:108px;border-width:6px;margin-right:22px}
  .hero .brand-name{font-size:62px}
  .hero .brand-tagline{font-size:26px;margin-top:8px}

  /* business cards */
  .card{position:absolute;left:40px;width:310px;height:200px;box-shadow:0 3px 8px rgba(0,0,0,.35);overflow:hidden}
  .card-front{top:620px}
  .card-back{top:880px;background:var(--paper)}
  .card::after{content:"";position:absolute;left:0;right:0;bottom:0;height:6px;background:var(--red)}
  .card-front .brand{left:30px;top:70px}
  .card-front .brand-dot{width:50px;height:50px;border-width:3px;margin-right:12px}
  .card-front .brand-name{font-size:29px}
  .card-front .brand-tagline{font-size:12px;margin-top:3px}

  .card-back .rule{position:absolute;left:0;right:0;top:62px;height:1px;background:var(--rule)}
  .card-back .brand-dot{position:absolute;left:42px;top:38px;width:50px;height:50px;border:3px solid var(--red);border-radius:50%;background:var(--paper)}
  .card-back .person{position:absolute;left:150px;top:76px;color:var(--red);font-size:10px;line-height:1.3}
  .card-back .contact{position:absolute;left:150px;top:124px;font-size:10px;line-height:1.25}

  .icon-line{display:flex;align-items:center;gap:3px}
  .icon-line svg{flex:none}

  /* letterhead */
  .sheet{position:absolute;left:420px;top:537px;width:441px;height:624px;background:var(--paper);box-shadow:3px 4px 10px rgba(0,0,0,.35)}
  .sheet .brand{left:42px;top:26px}
  .sheet .brand-dot{width:40px;height:40px;border-width:2.5px;margin-right:9px}
  .sheet .brand-name{font-size:21px}
  .sheet .brand-tagline{font-size:9px;margin-top:2px}
  .sheet .side-rule{position:absolute;left:413px;top:0;bottom:0;width:1px;background:var(--rule)}
  .sheet .side-dot{position:absolute;left:398px;top:140px;width:31px;height:31px;border:2px solid var(--red);border-radius:50%;background:var(--paper)}
  .sheet .sender{position:absolute;left:55px;top:102px;font-size:4.6px;white-space:nowrap}
  .sheet .address-mark{position:absolute;width:1.5px;height:1.5px;background:var(--ink)}
  .sheet .fold{position:absolute;left:0;width:16px;height:1px;background:var(--rule)}
  .sheet .meta{position:absolute;left:292px;font-size:6.3px;line-height:1.3}
  .sheet .meta-top{top:28px}
  .sheet .meta-bank{top:573px}
</style>
</head>
<body>

<section class="hero dark">
  <div class="brand">
    <span class="brand-dot"></span>
    <div>
      <div class="brand-name">Thermfeld</div>
      <div class="brand-tagline">effizient. nachhaltig. verlässlich</div>
    </div>
  </div>
</section>

<section class="card card-front dark">
  <div class="brand">
    <span class="brand-dot"></span>
    <div>
      <div class="brand-name">Thermfeld</div>
      <div class="brand-tagline">effizient. nachhaltig. verlässlich</div>
    </div>
  </div>
</section>

<section class="card card-back">
  <div class="rule"></div>
  <span class="brand-dot"></span>
  <div class="person">Max Mustermann<br>Geschäftsführer<br>Thermfeld</div>
  <div class="contact">
    <div>Musterweg 10</div>
    <div>12345 Musterstadt</div>
    <div class="icon-line"><svg width="9" height="9" viewBox="0 0 24 24"><path fill="#1d1d1b" d="M6.6 10.8a15 15 0 0 0 6.6 6.6l2.2-2.2a1 1 0 0 1 1-.25 11.4 11.4 0 0 0 3.6.57 1 1 0 0 1 1 1V20a1 1 0 0 1-1 1A17 17 0 0 1 3 4a1 1 0 0 1 1-1h3.5a1 1 0 0 1 1 1c0 1.25.2 2.45.57 3.57a1 1 0 0 1-.25 1z"/></svg>+49 123 123 123 123</div>
    <div class="icon-line"><span>@</span>info@thermfeld.de</div>
    <div class="icon-line"><svg width="8" height="9" viewBox="0 0 16 20"><rect x="2" y="1" width="12" height="18" rx="6" fill="#1d1d1b"/><line x1="8" y1="2" x2="8" y2="8" stroke="#fff" stroke-width="1.5"/></svg>www.thermfeld.de</div>
  </div>
</section>

<section class="sheet">
  <div class="brand">
    <span class="brand-dot"></span>
    <div>
      <div class="brand-name">Thermfeld</div>
      <div class="brand-tagline">effizient. nachhaltig. verlässlich</div>
    </div>
  </div>

  <div class="meta meta-top">
    Max Mustermann<br>Geschäftsführer<br><br>
    Musterweg 10<br>12345 Musterstadt<br>
    <span class="icon-line"><svg width="6" height="6" viewBox="0 0 24 24"><path fill="#1d1d1b" d="M6.6 10.8a15 15 0 0 0 6.6 6.6l2.2-2.2a1 1 0 0 1 1-.25 11.4 11.4 0 0 0 3.6.57 1 1 0 0 1 1 1V20a1 1 0 0 1-1 1A17 17 0 0 1 3 4a1 1 0 0 1 1-1h3.5a1 1 0 0 1 1 1c0 1.25.2 2.45.57 3.57a1 1 0 0 1-.25 1z"/></svg>+049 123 123 123</span>
    <span class="icon-line"><span>@</span>info@thermfeld.de</span>
    <span class="icon-line"><svg width="5" height="6" viewBox="0 0 16 20"><rect x="2" y="1" width="12" height="18" rx="6" fill="#1d1d1b"/></svg>www.thermfeld.de</span>
  </div>

  <span class="address-mark" style="left:42px;top:96px"></span>
  <span class="address-mark" style="left:219px;top:96px"></span>
  <div class="sender">Steuerkanzlei Jonas Pelling • Musterstraße 123 • 12345 Hamburg</div>
  <span class="address-mark" style="left:42px;top:187px"></span>
  <span class="address-mark" style="left:219px;top:187px"></span>

  <span class="fold" style="top:220px"></span>
  <span class="fold" style="top:311px;left:10px;width:10px"></span>
  <span class="fold" style="top:441px"></span>

  <div class="side-rule"></div>
  <span class="side-dot"></span>

  <div class="meta meta-bank">
    Nordquell Bank Musterhausen eG<br>
    IBAN: DE 12 1234 1234 1234 1234 12<br>
    BIC: ABCDEFGHIJK<br>
    U-St.-Nr. 000 000 000
  </div>
</section>

</body>
</html>
```